PlayTallyCollective - Game Statistics and Achievement Tracking

I need a new modern design for an existing website.

The website is a project to track statistics and achievements for games (currently Vaporix Achievements/Stats and stats for Hauler Road Odyssey 2 and Frontier Rig Voyager).
I am currently expanding the site with other platforms (like KVL) and more games.
I am also adding a user registration/signin with user profiles to show off their achievements and stats across all platforms and games.

The current website is available at https://pltally.example/
To search for data you can use the username "quietfennel" (without quotes).

The design should be modern and extendable and contain space for a logo.

The logo should match the project. It should combine Gaming with statistics.

Target Market(s)

Video game players

Number of Pages Required

5+ page

Font styles to use
Sans Serif

Requirements
Must have
• Basic Layout, User profile page (not yet available on live site), Search Page for Platforms/Games, Platform profile page, Dark theme

```html
<!DOCTYPE html>
<html lang="en">
<head>
<meta charset="UTF-8">
<title>PlayTallyCollective – Game Statistics</title>
<link href="https://fonts.googleapis.com/css2?family=Open+Sans:wght@400;600;700&display=swap" rel="stylesheet">
<style>
:root{
  --red:#e3102f;
  --red-dark:#b80c25;
  --ink:#141014;
  --night:#120c14;
  --plum:#1e1220;
  --white:#ffffff;
  --paper:#ffffff;
  --text:#1b1b1b;
  --muted:#555;
  --line:#e3e3e3;
}
*{box-sizing:border-box;margin:0;padding:0}
html,body{width:1200px;height:3564px;overflow:hidden}
body{font-family:"Open Sans",Arial,sans-serif;color:var(--text);background:var(--paper);position:relative}
section,footer{position:absolute;left:0;width:1200px}
.abs{position:absolute}

/* hero */
.hero{top:0;height:640px;background:var(--night);overflow:hidden}
.hero-art{position:absolute;inset:0;background:
  radial-gradient(ellipse 260px 200px at 1000px 140px,rgba(80,200,70,.55),transparent 70%),
  radial-gradient(ellipse 300px 220px at 760px 120px,rgba(220,40,140,.35),transparent 70%),
  radial-gradient(ellipse 420px 260px at 880px 520px,rgba(40,90,90,.45),transparent 70%),
  linear-gradient(90deg,#07060a 0%,#0d0b12 45%,#1a1420 100%)}
.nav{position:absolute;left:72px;top:40px;width:1068px;height:64px;background:rgba(18,14,20,.82);border-radius:6px;display:flex;align-items:center;padding:0 28px}
.logo{font-weight:700;font-size:24px;color:var(--white)}
.nav-links{display:flex;gap:22px;margin-left:60px;list-style:none}
.nav-links li{font-size:14px;color:var(--white)}
.btn{background:var(--red);color:var(--white);font-weight:600;font-size:14px;border-radius:4px;display:inline-flex;align-items:center;gap:8px;justify-content:center}
.nav .btn{margin-left:auto;height:40px;padding:0 18px}
.hero h1{position:absolute;left:96px;top:300px;width:520px;font-size:46px;line-height:52px;font-weight:700;color:var(--white)}
.hero .lead{position:absolute;left:96px;top:470px;width:440px;font-size:15px;line-height:22px;color:#e8e8e8}
.search{background:var(--white);border-radius:6px;display:flex;align-items:center;padding:0 8px 0 18px;gap:12px;box-shadow:0 4px 14px rgba(0,0,0,.18)}
.search span{flex:1;font-size:15px;color:#666}
.search .btn{height:40px;padding:0 18px}
.hero .search{position:absolute;left:96px;top:556px;width:460px;height:60px}

/* offer */
.offer{top:640px;height:712px;background:var(--paper);text-align:center}
.section-title{font-size:44px;font-weight:400;color:var(--ink)}
.offer .section-title{margin-top:76px}
.offer .sub{width:520px;margin:18px auto 0;font-size:16px;line-height:26px;font-weight:600}
.cards{position:absolute;left:80px;top:228px;display:flex;gap:32px;text-align:left}
.card{width:328px;height:400px;background:var(--white);border-radius:6px;box-shadow:0 4px 18px rgba(0,0,0,.12);overflow:hidden}
.card-img{height:244px}
.card h3{font-size:18px;font-weight:700;margin:20px 16px 6px}
.card p{font-size:13px;line-height:18px;color:var(--muted);margin:0 16px}
.read-more{display:flex;align-items:center;gap:8px;margin:18px 16px 0;font-size:13px;font-weight:700;color:var(--red)}

/* how */
.how{top:1352px;height:488px;background:linear-gradient(180deg,#241425 0%,#1a1019 100%);color:var(--white)}
.how-art{position:absolute;left:580px;top:24px;width:590px;height:440px;border-radius:6px;background:
  radial-gradient(ellipse 200px 140px at 420px 120px,rgba(230,40,110,.35),transparent 70%),
  radial-gradient(ellipse 220px 160px at 150px 330px,rgba(120,40,160,.35),transparent 70%),
  linear-gradient(135deg,#2a1530,#140c18)}
.how h2{position:absolute;left:96px;top:104px;font-size:22px;font-weight:700}
.how .strong{position:absolute;left:96px;top:146px;width:420px;font-size:18px;line-height:27px;font-weight:700}
.how .body{position:absolute;left:96px;top:244px;width:430px;font-size:14px;line-height:20px;color:#e4dbe4}
.ticks{list-style:none}
.ticks li{display:flex;align-items:center;gap:10px;font-size:14px;line-height:22px}
.how .ticks{position:absolute;left:96px;top:318px}

/* feature */
.feature{top:1840px;height:688px;background:var(--paper)}
.feature-photo{position:absolute;left:208px;top:88px;width:372px;height:512px;background:linear-gradient(150deg,#c9c3bf 0%,#6b6f76 45%,#2f3136 100%)}
.feature .search{position:absolute;left:620px;top:150px;width:470px;height:58px}
.feature h2{position:absolute;left:624px;top:238px;width:480px;font-size:30px;line-height:38px;font-weight:600;color:var(--ink)}
.feature .body{position:absolute;left:624px;top:330px;width:480px;font-size:14px;line-height:21px;color:#333}
.feature .ticks{position:absolute;left:624px;top:428px}
.feature .ticks li{color:#222;line-height:26px}

/* projects */
.projects{top:2528px;height:592px;background:linear-gradient(180deg,#1d1019 0%,#160c14 100%);color:var(--white);text-align:center}
.projects .section-title{color:var(--white);margin-top:66px}
.projects .sub{width:440px;margin:14px auto 0;font-size:15px;line-height:22px}
.tile{position:absolute}
.t1{left:224px;top:192px;width:316px;height:180px;background:linear-gradient(135deg,#1b2a3a,#3c2236 60%,#0f0f16)}
.t2{left:556px;top:192px;width:224px;height:180px;background:linear-gradient(135deg,#1a3f5e,#2b2a50 55%,#0c0f1a)}
.t3{left:796px;top:192px;width:292px;height:180px;background:linear-gradient(135deg,#3a4c5a,#1e2a36 55%,#101418)}
.t4{left:128px;top:388px;width:552px;height:196px;background:linear-gradient(135deg,#0d1a2e,#4a1424 55%,#130a12)}
.t5{left:696px;top:388px;width:392px;height:196px;background:linear-gradient(135deg,#3a3636,#151313 60%,#0a0a0a)}

/* footer */
.footer{top:3120px;height:444px;background:var(--paper);text-align:center}
.footer h2{margin-top:70px;font-size:28px;font-weight:700;color:var(--ink)}
.footer .body{width:720px;margin:14px auto 0;font-size:14px;line-height:21px;color:#333}
.foot-links{display:flex;justify-content:center;margin-top:22px;list-style:none}
.foot-links li{font-size:14px;padding:0 12px;border-left:1px solid #999}
.foot-links li:first-child{border-left:none}
.social{display:flex;justify-content:center;gap:16px;margin-top:18px}
.social span{width:16px;height:16px;border-radius:50%;background:#222}
.footer hr{width:780px;margin:22px auto 0;border:none;border-top:1px solid var(--line)}
.copy{margin-top:16px;font-size:12px;color:#555}
</style>
</head>
<body>

<section class="hero">
  <div class="hero-art" role="img" aria-label="Dark gaming room with a neon-lit controller and glowing green and pink lights"></div>
  <nav class="nav">
    <div class="logo">PlayTallyCollective</div>
    <ul class="nav-links"><li>Home</li><li>About Us</li><li>Platforms</li><li>Games</li><li>Leaderboards</li></ul>
    <span class="btn">Sign In
      <svg width="14" height="14" viewBox="0 0 14 14" fill="none" stroke="#fff" stroke-width="1.6"><path d="M8 2h4v10H8M1 7h8M6 4l3 3-3 3"/></svg>
    </span>
  </nav>
  <h1>Track Your Achievements Across Platforms</h1>
  <p class="lead">Connect your favorite gaming accounts and explore your stats Master your progress and showcase your success in one place.</p>
  <div class="search">
    <svg width="18" height="18" viewBox="0 0 18 18" fill="none" stroke="#222" stroke-width="2"><circle cx="7.5" cy="7.5" r="5.5"/><path d="M12 12l4.5 4.5"/></svg>
    <span>Search your username or platform...</span>
    <span class="btn">Get Started</span>
  </div>
</section>

<section class="offer">
  <h2 class="section-title">What We Offer</h2>
  <p class="sub">Track Your Achievements, Compare With Friends, And Explore Your Gaming Progress Across Multiple Platforms With Our Comprehensive Services.</p>
  <div class="cards">
    <article class="card">
      <div class="card-img" role="img" aria-label="Player at a desk with a racing game on screen" style="background:linear-gradient(135deg,#2a3a6a,#6a4a8a 50%,#151522)"></div>
      <h3>Achievement Tracking &amp; Stats</h3>
      <p>Users Can Link Their Gaming Account (Vaporix, KVL, Zentra, Etc.) To Track Their Achievements, Compare Scores...</p>
      <span class="read-more">read more <svg width="12" height="10" viewBox="0 0 12 10" fill="none" stroke="#e3102f" stroke-width="2"><path d="M2 1l4 4-4 4M6 1l4 4-4 4"/></svg></span>
    </article>
    <article class="card">
      <div class="card-img" role="img" aria-label="Close-up of a gaming controller in neon light" style="background:linear-gradient(135deg,#1d3a2a,#3e2a44 55%,#0e0e14)"></div>
      <h3>Achievement Tracking &amp; Stats</h3>
      <p>Users Can Link Their Gaming Account (Vaporix, KVL, Zentra, Etc.) To Track Their Achievements, Compare Scores...</p>
      <span class="read-more">read more <svg width="12" height="10" viewBox="0 0 12 10" fill="none" stroke="#e3102f" stroke-width="2"><path d="M2 1l4 4-4 4M6 1l4 4-4 4"/></svg></span>
    </article>
    <article class="card">
      <div class="card-img" role="img" aria-label="Player wearing a headset in front of a monitor" style="background:linear-gradient(135deg,#c8c2c6,#7a6e80 50%,#2a2430)"></div>
      <h3>Achievement Tracking &amp; Stats</h3>
      <p>Users Can Link Their Gaming Account (Vaporix, KVL, Zentra, Etc.) To Track Their Achievements, Compare Scores...</p>
      <span class="read-more">read more <svg width="12" height="10" viewBox="0 0 12 10" fill="none" stroke="#e3102f" stroke-width="2"><path d="M2 1l4 4-4 4M6 1l4 4-4 4"/></svg></span>
    </article>
  </div>
</section>

<section class="how">
  <h2>How It Works</h2>
  <p class="strong">Easily Connect Your Gaming Accounts, Track Your Progress, And Explore Detailed Stats And Achievements!</p>
  <p class="body">Get Started By Creating An Account And Linking Your Gaming Profiles. Track Your Achievements And Explore Detailed Stats Across Popular Platforms Like Vaporix, KVL, And Zentra.</p>
  <ul class="ticks">
    <li><svg width="14" height="12" viewBox="0 0 14 12" fill="none" stroke="#e3102f" stroke-width="2.2"><path d="M1 6l4 4 8-9"/></svg>create an account or sign in</li>
    <li><svg width="14" height="12" viewBox="0 0 14 12" fill="none" stroke="#e3102f" stroke-width="2.2"><path d="M1 6l4 4 8-9"/></svg>connect your gaming accounts</li>
    <li><svg width="14" height="12" viewBox="0 0 14 12" fill="none" stroke="#e3102f" stroke-width="2.2"><path d="M1 6l4 4 8-9"/></svg>track achievements and stats</li>
    <li><svg width="14" height="12" viewBox="0 0 14 12" fill="none" stroke="#e3102f" stroke-width="2.2"><path d="M1 6l4 4 8-9"/></svg>join the community</li>
  </ul>
  <div class="how-art" role="img" aria-label="Illustration of a dark stats dashboard with achievement panels"></div>
</section>

<section class="feature">
  <div class="feature-photo" role="img" aria-label="Hands holding a handheld game console"></div>
  <div class="search">
    <svg width="18" height="18" viewBox="0 0 18 18" fill="none" stroke="#222" stroke-width="2"><circle cx="7.5" cy="7.5" r="5.5"/><path d="M12 12l4.5 4.5"/></svg>
    <span>Search your username or platform...</span>
    <span class="btn">Get Started</span>
  </div>
  <h2>As Opposed To Using Content Here, Content Here Making</h2>
  <p class="body">Less Normal Distribution Of Letters, As Opposed To Using 'Content Here, Content Here', Making It Look Like Readable English. Many Desktop Publishing Packages And Web Page Editors Now Use Lorem Ipsum As Their Default Model Text, And A Search</p>
  <ul class="ticks">
    <li><svg width="14" height="12" viewBox="0 0 14 12" fill="none" stroke="#e3102f" stroke-width="2.2"><path d="M1 6l4 4 8-9"/></svg>Lorem ipsum is that it has a more</li>
    <li><svg width="14" height="12" viewBox="0 0 14 12" fill="none" stroke="#e3102f" stroke-width="2.2"><path d="M1 6l4 4 8-9"/></svg>Lorem ipsum is that it has a more</li>
    <li><svg width="14" height="12" viewBox="0 0 14 12" fill="none" stroke="#e3102f" stroke-width="2.2"><path d="M1 6l4 4 8-9"/></svg>Lorem ipsum is that it has a more</li>
    <li><svg width="14" height="12" viewBox="0 0 14 12" fill="none" stroke="#e3102f" stroke-width="2.2"><path d="M1 6l4 4 8-9"/></svg>Lorem ipsum is that it has a more</li>
    <li><svg width="14" height="12" viewBox="0 0 14 12" fill="none" stroke="#e3102f" stroke-width="2.2"><path d="M1 6l4 4 8-9"/></svg>Lorem ipsum is that it has a more</li>
  </ul>
</section>

<section class="projects">
  <h2 class="section-title">Our Recent Projects</h2>
  <p class="sub">Lorem ipsum as their default model text, and a search for 'lorem ipsum' will uncover many infancy.</p>
  <div class="tile t1" role="img" aria-label="Gaming room with multiple screens"></div>
  <div class="tile t2" role="img" aria-label="Blue-lit gaming setup"></div>
  <div class="tile t3" role="img" aria-label="Player at a gaming event"></div>
  <div class="tile t4" role="img" aria-label="Esports arena with red and blue lights"></div>
  <div class="tile t5" role="img" aria-label="Hands holding a game controller"></div>
</section>

<footer class="footer">
  <h2>PlayTallyCollective</h2>
  <p class="body">Lorem ipsum is that it has a more-or-less normal distribution of letters, as opposed to using 'content here, content here', making it look like readable english. many desktop publishing packages and web page editors now use lorem ipsum as their default model text, and a search for</p>
  <ul class="foot-links"><li>Home</li><li>About Us</li><li>Platforms</li><li>Games</li><li>Leaderboards</li></ul>
  <div class="social" aria-label="Social links"><span></span><span></span><span></span></div>
  <hr>
  <p class="copy">© 2024 PlayTallyCollective</p>
</footer>

</body>
</html>
```